brevan promotion

We need a Flyer design for our panel beating shop (car smarsh repairer). Shop's name is "BREVAN PANELS".

address: 7 TALWEN ROAD, EPPING, VIC 3076
phone number: 0419637208

We have been in current location and serve the community for over 15 years. We pride ourselves on our service and quality,this is why we are one of the most strongest shops in the northern area and well known. We have the most up-to-date technologies to ensure all the body repair work we done is correct and customer satisfied. All the repair works we done is lifetime guaranteed. And we are the recommended repair for all insurance companies.

Currently EPPING and around area is in big development, more population moving in. We want more people to know that we are here and if they get invoved in an accident or damage on the car, they can give us a call and we will assisit.

The flyer should included the logo of the shop and some insurance companies. Represent our professional and friendly image. Show that we can help people to solve their problem. Bacause when accident happend, most people will feel helpless and dont know what to do. We want them know that all they need to do is give us a phone call and we will guide them to solve the problem.

Some Logo, pictures, and one side of the business card is provided as a reference.
Updates

Thanks for your submit. We are currently considering all the designing we have received.

Target Market(s)

The local resident

Industry/Entity Type

Insurance

Requirements
Must have
• Comapny Logo, insurance logo (see the logo provided as reference, but not bigger that company logo).
OUR ADDRESS AND CONTACT PHONE NUMBER

```html
<!DOCTYPE html>
<html lang="en">
<head>
<meta charset="utf-8">
<title>Brevan Panels – Flyer</title>
<link rel="stylesheet" href="https://fonts.googleapis.com/css2?family=Open+Sans:wght@400;700&family=Roboto+Condensed:ital,wght@0,700;1,700&display=swap">
<style>
  :root {
    --orange: #e8571c;
    --orange-deep: #dc4f14;
    --sky: #9dbfe3;
    --sky-light: #d9e7f5;
    --brick: #585c63;
    --brick-dark: #43464c;
    --white: #ffffff;
    --ink: #111111;
    --badge: #6b6f78;
  }
  * { margin: 0; padding: 0; box-sizing: border-box; }
  html, body { width: 1200px; height: 900px; overflow: hidden; background: var(--orange); }
  .flyer {
    position: relative;
    width: 1200px;
    height: 900px;
    overflow: hidden;
    background: var(--orange);
    font-family: "Open Sans", Arial, sans-serif;
    color: var(--white);
  }
  .shopfront {
    position: absolute;
    inset: 0 0 auto 0;
    height: 560px;
    background:
      linear-gradient(180deg, rgba(232,87,28,0) 0%, rgba(232,87,28,0) 52%, rgba(232,87,28,0.85) 72%, var(--orange) 100%),
      linear-gradient(172deg, var(--sky-light) 0%, var(--sky) 12%, var(--brick) 24%, var(--brick-dark) 60%, var(--brick) 100%);
  }
  .street-name {
    position: absolute;
    left: 20px;
    top: 72px;
    display: flex;
    align-items: center;
    gap: 14px;
    transform: rotate(-8deg);
    font-family: "Roboto Condensed", "Arial Narrow", sans-serif;
    font-style: italic;
    font-weight: 700;
    font-size: 46px;
    letter-spacing: 3px;
    color: rgba(255,255,255,0.9);
    text-shadow: 0 2px 4px rgba(0,0,0,0.3);
  }
  .street-name::before, .street-name::after {
    content: "";
    display: block;
    height: 3px;
    background: rgba(255,255,255,0.85);
  }
  .street-name::before { width: 46px; }
  .street-name::after { width: 420px; }
  .street-number {
    position: absolute;
    left: 80px;
    top: 220px;
    font-family: "Roboto Condensed", "Arial Narrow", sans-serif;
    font-weight: 700;
    font-size: 26px;
    color: var(--white);
  }
  .shop-sign {
    position: absolute;
    left: 350px;
    top: 150px;
    font-family: "Roboto Condensed", "Arial Narrow", sans-serif;
    font-weight: 700;
    font-size: 104px;
    line-height: 1;
    color: var(--white);
    transform: rotate(-3deg);
    transform-origin: left bottom;
  }
  .sign-rule {
    position: absolute;
    left: 330px;
    top: 300px;
    width: 790px;
    height: 14px;
    background: var(--orange);
    transform: rotate(-3deg);
    transform-origin: left center;
  }
  .about {
    position: absolute;
    left: 46px;
    top: 460px;
    width: 460px;
    font-size: 21.5px;
    line-height: 1.26;
    text-align: justify;
    text-align-last: right;
    color: var(--white);
  }
  .services {
    position: absolute;
    left: 540px;
    top: 360px;
    width: 500px;
    list-style: none;
    text-align: center;
    font-family: "Roboto Condensed", "Arial Narrow", sans-serif;
    font-weight: 700;
    text-transform: uppercase;
    color: var(--white);
    text-shadow: 2px 3px 3px rgba(0,0,0,0.55);
  }
  .services li { font-size: 38px; line-height: 1; margin-bottom: 48px; }
  .services li.services__feature { font-size: 46px; line-height: 1.15; margin-top: 4px; }
  .call-now {
    position: absolute;
    left: 1155px;
    top: 592px;
    transform: translate(-50%, -50%) rotate(-90deg);
    white-space: nowrap;
    font-family: "Roboto Condensed", "Arial Narrow", sans-serif;
    font-weight: 700;
    font-size: 44px;
    letter-spacing: 4px;
    color: var(--white);
    text-shadow: 1px 2px 3px rgba(0,0,0,0.35);
  }
  .repairer-code {
    position: absolute;
    left: 57px;
    top: 770px;
    width: 393px;
    text-align: center;
    font-weight: 700;
    font-size: 14px;
    color: var(--white);
  }
  .insurer-strip {
    position: absolute;
    left: 57px;
    top: 800px;
    width: 393px;
    height: 48px;
    background: var(--ink);
    display: flex;
    align-items: center;
    justify-content: space-between;
    padding: 0 12px;
  }
  .insurer-badge { display: block; width: 40px; height: 22px; border-radius: 3px; background: var(--badge); }
  .insurer-badge--round { width: 22px; border-radius: 50%; }
</style>
</head>
<body>
<main class="flyer">
  <div class="shopfront" role="img" aria-label="Photo of the Brevan Panels workshop building with its roller door under a blue sky"></div>

  <div class="street-name">TALWEN ROAD</div>
  <div class="street-number">No.7</div>
  <div class="sign-rule"></div>
  <h1 class="shop-sign">Brevan Panels</h1>

  <p class="about">We have the most up-to-date technologies to ensure all the body repair work we done is correct and customer satisfied. All the repair works we done is lifetime guaranteed. And we are the recommended repair for all insurance companies.</p>

  <ul class="services">
    <li>Insurance Work</li>
    <li>Private Work</li>
    <li>Free Onsite Quoting</li>
    <li>Free Loan Car</li>
    <li class="services__feature">Computer Colourised<br>System</li>
  </ul>

  <div class="call-now">CALL NOW - 0419637208</div>

  <p class="repairer-code">ROVANA/KESTRA REPAIRER CODE #40736</p>
  <div class="insurer-strip" aria-label="Approved insurer partners">
    <span class="insurer-badge"></span>
    <span class="insurer-badge"></span>
    <span class="insurer-badge"></span>
    <span class="insurer-badge insurer-badge--round"></span>
    <span class="insurer-badge insurer-badge--round"></span>
    <span class="insurer-badge"></span>
    <span class="insurer-badge"></span>
    <span class="insurer-badge insurer-badge--round"></span>
  </div>
</main>
</body>
</html>
```